Bold and Eye Catching Beef Jerky Stick Label

This will be a label for beef jerky sticks. It is a sweet and spicy flavor called "Tango Drift". I have included the company logo which I would like to be included somewhere in the design. I would like the label to be bold and eye catching. This product's price category needs a high volume of sales, so the more this attracts peoples attention the better.

This label will go on vacuum sealed jerky sticks that are packaged for individual retail sale. I will need the design to be oriented so the label is vertical ( 3.5" tall 2" wide).

The flavor is a mixture of brown sugar and cayenne pepper.

Target Market(s)

male all ages

Industry/Entity Type

Food Store

Font styles to use
Sans Serif

Requirements
Must have
• company logo somewhere in the design, preferably at the top. Must also have the flavor name "Tango Drift" somewhere.
Nice to have
• I would like it to be bold and eye catching. The rocky dale wrapper would be a good starting point for ideas.

```html
<!DOCTYPE html>
<html lang="en">
<head>
<meta charset="utf-8">
<title>Copper Mesa Meat – Beef Jerky Stick, Tango Drift</title>
<link rel="stylesheet" href="https://fonts.googleapis.com/css2?family=Open+Sans:wght@400;700&family=Oswald:wght@600&family=Lobster&display=swap">
<style>
  :root {
    --label-red: #c8180f;
    --label-deep: #9a0d08;
    --flame-orange: #f79a1e;
    --flame-glow: #ffe27a;
    --cream: #fff4e0;
    --panel-tan: #f2b564;
    --brown: #6a2218;
    --ink: #2a1c18;
    --gold: #ffe400;
    --ribbon-red: #d42a1c;
    --ribbon-dark: #8e2114;
  }
  html, body {
    margin: 0;
    padding: 0;
    width: 724px;
    height: 1200px;
    overflow: hidden;
    background: #ffffff;
  }
  .label {
    position: relative;
    width: 724px;
    height: 1200px;
    overflow: hidden;
    background:
      radial-gradient(ellipse 120px 300px at 0% 58%, var(--flame-glow) 0%, var(--flame-orange) 35%, rgba(247,154,30,0) 100%),
      radial-gradient(ellipse 120px 300px at 100% 58%, var(--flame-glow) 0%, var(--flame-orange) 35%, rgba(247,154,30,0) 100%),
      linear-gradient(180deg, var(--label-deep) 0%, var(--label-red) 30%, #e0400f 60%, var(--label-red) 85%, var(--label-deep) 100%);
  }
  .label__frame {
    position: absolute;
    inset: 0;
  }
  .brand {
    position: absolute;
    left: 0;
    width: 724px;
    top: 420px;
    text-align: center;
    font-family: "Open Sans", Arial, sans-serif;
    font-weight: 700;
    color: var(--ink);
  }
  .brand__name {
    display: block;
    font-size: 44px;
    line-height: 1;
    letter-spacing: 0.5px;
  }
  .brand__sub {
    display: block;
    margin-top: 14px;
    font-size: 19px;
    letter-spacing: 9px;
    padding-left: 9px;
  }
  .product-name {
    position: absolute;
    left: 0;
    width: 724px;
    top: 584px;
    margin: 0;
    text-align: center;
    font-family: "Oswald", "Arial Narrow", sans-serif;
    font-weight: 600;
    font-size: 66px;
    line-height: 1;
    color: var(--brown);
    text-transform: uppercase;
    transform: scaleY(1.05);
  }
  .flavor {
    position: absolute;
    left: 0;
    width: 724px;
    top: 760px;
    margin: 0;
    text-align: center;
    font-family: "Lobster", cursive;
    font-weight: 400;
    font-size: 72px;
    line-height: 1;
    color: var(--gold);
    transform: rotate(-6deg);
  }
  .mascot {
    position: absolute;
    left: 309px;
    top: 915px;
    width: 110px;
    height: 110px;
    border-radius: 40% 40% 45% 45%;
    background: radial-gradient(circle at 50% 45%, #8a3a24 0%, var(--brown) 70%);
  }
</style>
</head>
<body>
<main class="label">
  <svg class="label__frame" width="724" height="1200" viewBox="0 0 724 1200" aria-hidden="true">
    <defs>
      <radialGradient id="panelFill" cx="50%" cy="55%" r="60%">
        <stop offset="0%" stop-color="#fffaf0"/>
        <stop offset="45%" stop-color="#fbdcae"/>
        <stop offset="100%" stop-color="#f0ad58"/>
      </radialGradient>
    </defs>
    <!-- shield panel -->
    <path class="panel-outline"
      d="M362,122 C255,124 175,175 140,240 Q120,280 72,280 L61,280 L61,968 L72,968 Q120,968 140,1000 C175,1060 255,1099 362,1099 C469,1099 549,1060 584,1000 Q604,968 652,968 L663,968 L663,280 L652,280 Q604,280 584,240 C549,175 469,124 362,122 Z"
      fill="url(#panelFill)" stroke="#6a2218" stroke-width="14"/>
    <path
      d="M362,122 C255,124 175,175 140,240 Q120,280 72,280 L61,280 L61,968 L72,968 Q120,968 140,1000 C175,1060 255,1099 362,1099 C469,1099 549,1060 584,1000 Q604,968 652,968 L663,968 L663,280 L652,280 Q604,280 584,240 C549,175 469,124 362,122 Z"
      fill="none" stroke="#ffe400" stroke-width="5"/>
    <path
      d="M362,122 C255,124 175,175 140,240 Q120,280 72,280 L61,280 L61,968 L72,968 Q120,968 140,1000 C175,1060 255,1099 362,1099 C469,1099 549,1060 584,1000 Q604,968 652,968 L663,968 L663,280 L652,280 Q604,280 584,240 C549,175 469,124 362,122 Z"
      fill="none" stroke="#6a2218" stroke-width="2" transform="translate(362 610) scale(0.965 0.975) translate(-362 -610)"/>

    <!-- brand mark: plain circle -->
    <circle cx="364" cy="290" r="100" fill="#ffffff" stroke="#6a2218" stroke-width="6"/>
    <circle cx="364" cy="290" r="88" fill="#6a2218"/>

    <!-- ribbon tails -->
    <polygon points="32,770 170,752 182,860 48,876 78,826" fill="#8e2114" stroke="#ffe400" stroke-width="4" stroke-linejoin="round"/>
    <polygon points="556,700 687,686 652,740 696,790 568,806" fill="#8e2114" stroke="#ffe400" stroke-width="4" stroke-linejoin="round"/>
    <!-- ribbon folds -->
    <polygon points="170,752 182,860 110,884 97,794" fill="#5e150c"/>
    <polygon points="556,700 568,806 627,820 627,737" fill="#5e150c"/>
    <!-- ribbon band -->
    <polygon points="97,794 627,737 627,820 97,884" fill="#d42a1c" stroke="#ffe400" stroke-width="4" stroke-linejoin="round"/>
  </svg>

  <div class="brand">
    <span class="brand__name">COPPER MESA MEAT</span>
    <span class="brand__sub">MANUFACTURING</span>
  </div>

  <h1 class="product-name">Beef Jerky Stick</h1>

  <p class="flavor">Tango Drift</p>

  <div class="mascot" role="img" aria-label="Small steer head emblem"></div>
</main>
</body>
</html>
```